Selbsthilfegruppe für organtransplantierte Personen sucht Flyer-Design
Sehr schnelle Reaktion auf Änderungswünsche und top Support bis zum Druck :) Gerne wieder!
Zielgruppe
Wir sind eine Selbsthilfegruppe für organtransplantierte Personen, Zielgruppe sind Personen aus der Region die auch ein Spenderorgan empfangen haben und deren Angehörige, die Beistand und Information suchen sowie gemeinsame Aktivitäten wahrnehmen möchten.
Aufgabenstellung
Es gibt bereits einen Flyer der jedoch überarbeitet und etwas schöner und moderner gestaltet werden soll. Der Text kann bestehen bleiben und die Aufteilung muss nicht zwingend geändert werden, anstelle der aktuellen Fotos sollen dann andere eingefügt werden, die übergeben werden, sobald das Design akzeptiert wurde. Es geht hauptsächlich um das Design selbst, es soll ansprechen, freundlich, modern und hoffnungsvoll sein, die Grundfarbe sollte grün sein. Das Logo kann beibehalten aber farblich auch gerne angepasst werden. Es soll ein normaler Faltflyer sein, 2 Faltungen und damit vorn und hinten je 3 einzelne Bereiche wie aktuell, Gesamtmaß A4. Bei Rückfragen gerne melden!

```html
<!DOCTYPE html>
<html lang="de">
<head>
<meta charset="utf-8">
<title>Faltflyer Innenseite – Selbsthilfegruppe</title>
<link rel="stylesheet" href="https://fonts.googleapis.com/css2?family=Questrial&family=Pinyon+Script&display=swap">
<style>
  :root {
    --green: #00923f;
    --green-mid: #4a9f32;
    --orange: #e8961c;
    --orange-text: #e38a12;
    --white: #ffffff;
    --stage: #d9d9d9;
  }
  html, body {
    margin: 0;
    width: 1200px;
    height: 675px;
    overflow: hidden;
    background: var(--stage);
  }
  .flyer {
    position: absolute;
    left: 139px;
    top: 12px;
    width: 922px;
    height: 651px;
    background: var(--white);
    overflow: hidden;
    font-family: "Questrial", sans-serif;
  }
  .flyer-shapes {
    position: absolute;
    inset: 0;
  }
  .script-title {
    position: absolute;
    margin: 0;
    font-family: "Pinyon Script", cursive;
    font-weight: 400;
    color: var(--orange-text);
    font-size: 40px;
    line-height: 1;
    border-bottom: 1px solid var(--orange-text);
    padding: 0 1px 1px;
  }
  .title-about { left: 153px; top: 58px; }
  .title-together { left: 384px; top: 30px; }
  .about {
    position: absolute;
    left: 31px;
    top: 121px;
    width: 290px;
  }
  .about-block { margin: 0 0 19px; }
  .about-block h3 {
    margin: 0;
    font-weight: 700;
    font-size: 15.5px;
    line-height: 19.7px;
    color: var(--green);
    -webkit-text-stroke: 0.3px var(--green);
  }
  .about-block p {
    margin: 0;
    font-size: 15.5px;
    line-height: 19.7px;
    color: var(--orange-text);
  }
  .activity-label {
    position: absolute;
    font-size: 15.5px;
    color: var(--orange-text);
    line-height: 1;
  }
  .label-inform { right: calc(922px - 582px); top: 176px; }
  .label-discuss { left: 325px; top: 327px; }
  .label-celebrate { right: calc(922px - 582px); top: 476px; }
  .outreach {
    position: absolute;
    left: 603px;
    top: 547px;
    width: 330px;
    margin: 0;
    text-align: center;
    color: var(--white);
    font-size: 15.5px;
    line-height: 19.7px;
  }
</style>
</head>
<body>
<main class="flyer">
  <svg class="flyer-shapes" width="922" height="651" viewBox="0 0 922 651">
    <defs>
      <linearGradient id="top-swoosh" x1="0" y1="0" x2="1" y2="0">
        <stop offset="0" stop-color="#eea21c"/>
        <stop offset="0.55" stop-color="#7aa82c"/>
        <stop offset="1" stop-color="#00923f"/>
      </linearGradient>
      <linearGradient id="bottom-band" x1="0" y1="0" x2="1" y2="0">
        <stop offset="0" stop-color="#00923f"/>
        <stop offset="0.44" stop-color="#00923f"/>
        <stop offset="0.72" stop-color="#6fa52e"/>
        <stop offset="1" stop-color="#eaa01c"/>
      </linearGradient>
      <linearGradient id="hands-photo" x1="0" y1="0" x2="0" y2="1">
        <stop offset="0" stop-color="#c9a58e"/>
        <stop offset="0.45" stop-color="#c98f6f"/>
        <stop offset="0.8" stop-color="#a98a7c"/>
        <stop offset="1" stop-color="#e6e2e0"/>
      </linearGradient>
    </defs>

    <path d="M0 0 H429 Q170 45 0 119 Z" fill="url(#top-swoosh)"/>

    <rect x="613" y="0" width="309" height="520" fill="url(#hands-photo)"
          role="img" aria-label="Foto: viele übereinandergelegte Hände als Zeichen des Zusammenhalts"/>

    <path d="M0 593 Q520 540 922 413 V651 H0 Z" fill="url(#bottom-band)"/>
    <path d="M613 512 Q800 470 922 413 V400 H613 Z" fill="none"/>
    <path d="M600 520 Q790 482 922 410" fill="none" stroke="var(--white)" stroke-width="4"/>

    <g class="activity" fill="none" stroke="var(--green)" stroke-width="2.5">
      <circle cx="416" cy="148" r="46" fill="#b9a28c"
              role="img" aria-label="Foto: Publikum bei einem Fachvortrag"/>
      <line x1="420" y1="194" x2="582" y2="194"/>

      <circle cx="501" cy="298" r="46" fill="#a39a8e"
              role="img" aria-label="Foto: Gesprächsrunde im Stuhlkreis"/>
      <line x1="325" y1="345" x2="501" y2="345"/>

      <circle cx="416" cy="448" r="46" fill="#c7aa8f"
              role="img" aria-label="Foto: Gruppe beim gemeinsamen Feiern"/>
      <line x1="420" y1="494" x2="582" y2="494"/>
    </g>
  </svg>

  <h2 class="script-title title-about">Über uns</h2>
  <h2 class="script-title title-together">Gemeinsam</h2>

  <section class="about">
    <div class="about-block">
      <h3>Wir sind ...</h3>
      <p>eine Gruppe von Betroffenen<br>und deren Angehörige.</p>
    </div>
    <div class="about-block">
      <h3>Wir möchten ...</h3>
      <p>Erfahrungen austauschen,<br>Fachvorträge besuchen, aber nicht<br>nur über Krankheit reden, sondern<br>auch miteinander fröhlich sein.</p>
    </div>
    <div class="about-block">
      <h3>Wir organisieren gemeinsam ...</h3>
      <p>regelmäßige Treffen, Fachvorträge,<br>Infoveranstaltungen, gesellige<br>Zusammenkünfte und einiges mehr.</p>
    </div>
    <div class="about-block">
      <h3>Wir treffen uns ...</h3>
      <p>regelmäßig am letzten Dienstag<br>des Monats um 15:00 Uhr im<br>Familienzentrum ‚Mathilde‘,<br>Birkenweg 12 in Bad<br>Lindenau.</p>
    </div>
  </section>

  <span class="activity-label label-inform">... informieren</span>
  <span class="activity-label label-discuss">... diskutieren</span>
  <span class="activity-label label-celebrate">... feiern</span>

  <p class="outreach">... wollen wir mit öffentlichen<br>Aktionen viele Menschen erreichen<br>und über unsere Arbeit informieren.</p>
</main>
</body>
</html>
```